Cruise Booking Website

Cruise search and booking website

This project is a redesign of a cruise booking website we did a few years ago.

The current website is located here: http://voyage.pelicodeworks.net/en/

It's not fully functional but gives you ad idea how miserable the old design was.

All the information about cruises, cruise lines, destinations, ports and shore excursions will be similar to http://www.sailvexa.com/
Actual search pages (form, results, single result, sailing and cabin selection, ship info, booking) will have EXACTLY the same info as sailvexa.com

We like the style of http://harborquillnest.com, it's quite modern, good spacing, not overloaded with information. So you can use it as an example of what we like, not what we want as a final result for us. Please, don't copy it. The result should not be possible to resemble the harborquillnest.com, because our site has to be unique. This is important!
If you submit a design that clearly reminds another cruise site it will be rejected!

Also the mockup provided is just to give you the basic structure and show what information has to be present on the page. It doesn't mean the layout has to be the same as a mockup. The layout is up to the designer.

I've updated the mockup to be more generic so it doesn't confuse you:
https://files.example-vault.net/s/k7q2mzt9wp41xbr/Home%20page.png

When you're adding social sharing icons like facebook/twitter you have to use chinese ones instead:
https://files.example-vault.net/s/h3fn8dlq2zvy6ta/chinese-social-icons.png
Originals: http://shrtlk.example/qR7m

We'll start with home page first and after it's approved inner pages can be designed.

I know the cost of the project doesn't look high, but the task is straight forward and doesn't require to be very original, it's better to follow existing design and layout patterns that proved to work well.
That's why I encourage you to choose a template to build the design on top of one of https://themelattice.example/ themes if it will save the design work, will be easier and faster for you. So it will be more like a customization than a new design from scratch.

Mockups, site map and logo files:
- https://files.example-vault.net/sh/w4tp71bzqe0nmdv/QxrhKp8Zad

Website tree:
- https://papers.example-office.net/document/d/8vLqT2mXcR5pW9nZbK4sYh7JdF3gA6eU0tN1oPiMwQyB/edit?usp=sharing
Updates

So far a lot of designs are just copying http://www.harborquillnest.com/ - we don't like it!

We like the style of harborquillnest.com, it's quite modern, good spacing, not overloaded with information. So you can use it as an example of what we like, not what we want as a final result for us. Please, don't copy it. The result should not be possible to resemble the harborquillnest.com, because our site has to be unique. This is important!

Target Market(s)

Chinese travellers

Industry/Entity Type

Build

Requirements
Must have
• * White, blue and red
* Large spacing, not too much information cramped into a small space like sailvexa.com or the current website
* More "hidden" info in popups, tabs and so on, so not to many things are visible at the same time
* Compatible with twitter bootstrap styling (for easier coding):
- http://gridlantern.example.io/framework/index.html
- http://skinmorrow.example/
* Feel free to propose to build the design on top of one of https://themelattice.example/ themes if it will save the design work, will be easier and faster for you

```html
<!DOCTYPE html>
<html lang="en">
<head>
<meta charset="utf-8">
<title>Voyaro Cruises</title>
<link href="https://fonts.googleapis.com/css2?family=Open+Sans:wght@400;600&family=Signika:wght@300;400;600&family=Lobster&display=swap" rel="stylesheet">
<style>
:root{
  --sky:#1b78b8;
  --bar-dark:#222;
  --orange-top:#ffc21a;
  --orange-bottom:#f39a00;
  --red:#c41f2f;
  --blue-band:#2a93c8;
  --select-blue:#1f77b0;
  --page:#e8e8e8;
  --line:#bdbdbd;
  --text-red:#c41f2f;
  --text-blue:#1d6fa8;
  --white:#fff;
}
*{box-sizing:border-box;margin:0;padding:0}
html,body{width:1200px;height:900px;overflow:hidden}
body{position:relative;background:var(--page);font-family:"Open Sans",Arial,sans-serif;color:#333}
.abs{position:absolute}

.top-strip{left:0;top:0;width:1200px;height:10px;background:var(--sky)}
.util-bar{left:0;top:10px;width:1200px;height:20px;background:linear-gradient(#444,#111)}
.util-link{top:3px;font-size:10.5px;color:#ddd;letter-spacing:.5px;display:flex;align-items:center;gap:5px}
.social{top:5px;width:10px;height:9px;border-radius:2px}

.main-nav{left:0;top:30px;width:1200px;height:33px;background:linear-gradient(var(--orange-top),var(--orange-bottom));border-bottom:1px solid #c97800}
.main-nav ul{list-style:none;display:flex;position:absolute;left:124px;top:0;height:33px}
.main-nav li{height:33px;line-height:31px;font-family:"Signika",sans-serif;font-weight:300;font-size:17px;color:#3a2200;text-align:center;border-right:1px solid #e08a00}
.main-nav li.active{background:var(--red);color:var(--white)}

.hero{left:0;top:63px;width:1200px;height:468px;
  background:
    radial-gradient(ellipse 260px 120px at 62% 80%,rgba(240,243,246,.95),rgba(240,243,246,0) 100%),
    radial-gradient(ellipse 180px 70px at 60% 52%,rgba(255,255,255,.8),rgba(255,255,255,0) 100%),
    radial-gradient(ellipse 220px 60px at 12% 72%,rgba(255,255,255,.85),rgba(255,255,255,0) 100%),
    radial-gradient(ellipse 260px 80px at 28% 88%,rgba(140,200,220,.8),rgba(140,200,220,0) 100%),
    radial-gradient(ellipse 160px 60px at 83% 68%,rgba(255,255,255,.75),rgba(255,255,255,0) 100%),
    linear-gradient(180deg,#1668ad 0%,#2f80c2 30%,#5d9fd2 55%,#8dbde2 68%,#2a74b3 82%,#165e9c 100%);}
.slider-dots{left:1033px;top:76px;display:flex;gap:7px}
.slider-dots i{width:5px;height:5px;border-radius:50%;background:#1c4f7a}
.slider-dots i.on{background:#fff}
.promo-line{left:587px;top:0;width:2px;height:140px;background:var(--red)}
.promo-badge{left:545px;top:137px;width:90px;height:90px;border-radius:50%;background:var(--red);color:#fff;text-align:center;font-family:"Signika",sans-serif}
.promo-badge small{display:block;margin-top:20px;font-size:12px}
.promo-badge b{font-size:22px}
.promo-badge em{font-style:normal;font-size:11px}
.promo-tip{left:582px;top:224px;width:0;height:0;border-left:8px solid transparent;border-right:8px solid transparent;border-top:8px solid var(--red)}
.promo-caption{left:512px;top:237px;font-size:12px;color:#fff}

.brand-box{left:124px;top:336px;width:160px;height:195px;background:linear-gradient(#fafafa,#d5d5d5);border:1px solid #aaa;text-align:center}
.brand-mark{display:block;margin:20px auto 0;width:110px;height:110px;border-radius:50%;background:var(--select-blue)}
.brand-name{display:block;margin-top:16px;font-family:"Signika",sans-serif;font-weight:600;font-size:26px;color:var(--select-blue)}

.search-tabs{left:0;top:531px;width:1200px;height:31px;background:#333}
.search-tab{top:8px;font-size:12.5px;color:#ddd}
.search-tab.active{left:124px;top:-8px;width:74px;height:39px;background:var(--bar-dark);color:#fff;text-align:center;line-height:48px}
.tab-pointer{left:155px;top:562px;border-left:6px solid transparent;border-right:6px solid transparent;border-top:8px solid var(--bar-dark);width:0;height:0}
.phone{left:836px;top:533px;font-family:"Signika",sans-serif;font-weight:300;font-size:22px;color:#9fc6e4;display:flex;align-items:center;gap:6px}
.search-band{left:0;top:562px;width:1200px;height:70px;background:var(--blue-band)}
.select{top:581px;height:26px;background:var(--select-blue);border:1px solid #e6f2fa;color:#fff;font-size:11px;line-height:24px;padding-left:8px}
.select::after{content:"";position:absolute;right:0;top:0;width:19px;height:24px;border-left:1px solid #e6f2fa;background:var(--select-blue)}
.select i{position:absolute;right:6px;top:7px;width:6px;height:6px;border-right:2px solid #fff;border-bottom:2px solid #fff;transform:rotate(45deg);z-index:1}
.search-go{left:990px;top:545px}

.content-tabs{left:123px;top:654px;width:620px;height:35px;border-bottom:1px solid var(--line)}
.ctab{top:0;height:35px;line-height:42px;text-align:center;font-size:12px;border:1px solid var(--line);border-bottom:none}
.ctab.featured{left:0;width:148px;background:var(--page);color:var(--text-blue);font-weight:600;height:36px}
.ctab.offers{left:162px;width:136px;color:#777;font-size:12.5px;background:#ececec}
.feature-photo{left:126px;top:723px;width:312px;height:190px;border:3px solid #fff;background:linear-gradient(160deg,#4f86ab 0%,#8fbccb 35%,#e0d6b0 50%,#3f7a3e 70%,#2f5e32 100%)}
.trip-title{left:476px;top:715px;font-family:"Signika",sans-serif;font-size:23px;color:var(--text-red)}
.trip-points{left:476px;top:749px;font-size:11px;color:var(--text-blue);display:flex;gap:6px;align-items:center}
.trip-list{left:476px;top:797px;list-style:none;font-size:12px;color:var(--text-red)}
.trip-list li{height:30px;line-height:20px;display:flex;align-items:baseline;gap:8px}
.trip-list li::before{content:">";color:#333;font-size:11px}
.trip-list .price{font-family:"Signika",sans-serif;font-size:23px;line-height:20px;margin-left:-4px}
.divider{left:760px;top:654px;width:1px;height:246px;background:var(--line)}

.contest{left:807px;top:659px;width:268px;height:164px;background:#fff;padding:6px}
.contest-photo{width:256px;height:152px;background:linear-gradient(90deg,#5d8cad 0%,#c9a688 30%,#8fb2cc 55%,#2a4f75 75%,#1d3552 100%);position:relative}
.contest-copy{position:absolute;left:152px;top:34px;color:#fff;font-family:"Signika",sans-serif;line-height:1}
.contest-copy .s{font-size:12px}
.contest-copy .big{font-size:28px;margin-top:4px}
.best-offer{left:776px;top:772px}
.newsletter{left:776px;top:870px;width:300px;text-align:center;font-family:"Signika",sans-serif;font-size:22px;color:var(--text-blue);border-bottom:1px solid var(--line);height:30px}
</style>
</head>
<body>
<div class="abs top-strip"></div>
<div class="abs util-bar">
  <span class="abs util-link" style="left:688px">
    <svg width="10" height="12" viewBox="0 0 10 12"><path d="M5 11 C2 7 1 5.5 1 4.2 A4 4 0 0 1 9 4.2 C9 5.5 8 7 5 11Z" fill="none" stroke="#ddd"/><circle cx="5" cy="4.2" r="1.4" fill="#ddd"/></svg>Location Finder</span>
  <span class="abs util-link" style="left:828px">
    <svg width="11" height="11" viewBox="0 0 11 11"><circle cx="5.5" cy="3.5" r="2.5" fill="none" stroke="#ddd"/><path d="M1 11 C1 7 10 7 10 11" fill="none" stroke="#ddd"/></svg>My Account</span>
  <span class="abs social" style="left:1046px;background:#9cc4e4"></span>
  <span class="abs social" style="left:1062px;background:#5fb2e8"></span>
</div>

<nav class="abs main-nav">
  <ul>
    <li class="active" style="width:64px">Blog</li>
    <li style="width:130px">Cruise Info</li>
    <li style="width:180px">Specialty Cruises</li>
    <li style="width:153px">Destinations</li>
    <li style="width:80px">Lines</li>
    <li style="width:97px">Deals</li>
    <li style="width:90px">Ports</li>
    <li style="width:158px">Quote Request</li>
  </ul>
</nav>

<div class="abs hero" role="img" aria-label="Large white cruise ship sailing on a blue sea under a bright sky with clouds and splashing waves"></div>
<div class="abs slider-dots"><i class="on"></i><i></i><i></i><i></i></div>
<div class="abs promo-line"></div>
<div class="abs promo-badge"><small>SAVE</small><b>40%</b> <em>Off</em></div>
<div class="abs promo-tip"></div>
<div class="abs promo-caption">Lorem ipsum dolor sit amet &nbsp;&gt;</div>

<div class="abs brand-box">
  <span class="brand-mark"></span>
  <span class="brand-name">Voyaro</span>
</div>

<div class="abs search-tabs">
  <span class="abs search-tab active">Cruises</span>
  <span class="abs search-tab" style="left:201px">Air</span>
  <span class="abs search-tab" style="left:243px">Hotel</span>
  <span class="abs search-tab" style="left:299px">Car</span>
</div>
<div class="abs phone">
  <svg width="14" height="12" viewBox="0 0 14 12"><path d="M1 4 C1 1 13 1 13 4 L10 5 L10 3.5 L4 3.5 L4 5Z M3 6 L11 6 L12 11 L2 11Z" fill="#9fc6e4"/></svg>4008 512 390</div>
<div class="abs search-band"></div>
<div class="abs tab-pointer"></div>
<div class="abs select" style="left:123px;width:161px">Caribbean/Bahamas<i></i></div>
<div class="abs select" style="left:300px;width:118px">All Ports<i></i></div>
<div class="abs select" style="left:434px;width:136px">All Cruise Lines<i></i></div>
<div class="abs select" style="left:586px;width:158px">All Ships<i></i></div>
<div class="abs select" style="left:761px;width:100px">August 2013<i></i></div>
<div class="abs select" style="left:865px;width:95px">All Length<i></i></div>
<svg class="abs search-go" width="88" height="88" viewBox="0 0 88 88" aria-label="Search">
  <circle cx="44" cy="42" r="34" fill="#fff"/>
  <circle cx="44" cy="42" r="24" fill="var(--blue-band)"/>
  <circle cx="44" cy="42" r="13" fill="#fff"/>
  <path d="M40 35 L49 42 L40 49" fill="none" stroke="var(--blue-band)" stroke-width="3"/>
</svg>

<div class="abs content-tabs">
  <div class="abs ctab offers">Exceptional Offers</div>
  <div class="abs ctab featured">FEATURED</div>
</div>
<div class="abs feature-photo" role="img" aria-label="Aerial view of a tropical beach resort with palm trees and pools"></div>
<div class="abs trip-title">Japan 8 days</div>
<div class="abs trip-points">
  <svg width="11" height="11" viewBox="0 0 11 11"><rect x="1" y="4" width="9" height="6" fill="#c41f2f"/><rect x="0" y="2" width="11" height="3" fill="#a01020"/><rect x="5" y="2" width="1.5" height="8" fill="#fff"/></svg>
  This trip can earn you: 3000 points</div>
<ul class="abs trip-list">
  <li>Special rates for guests 55 years and older</li>
  <li>Rates from <span class="price">$209</span></li>
  <li>Kids 11 and Under Sail Free</li>
</ul>
<div class="abs divider"></div>

<div class="abs contest">
  <div class="contest-photo" role="img" aria-label="Couple relaxing on the deck of a sailboat">
    <div class="contest-copy"><div class="s">Enter &amp; Win</div><div class="big">$ 6000</div><div class="big">CRUISE</div><div class="s" style="margin-top:4px">Vacation For 2</div></div>
  </div>
</div>
<svg class="abs best-offer" width="104" height="72" viewBox="0 0 104 72">
  <path d="M8 10 L52 0 L96 10 L92 46 L52 68 L12 46Z" fill="var(--red)" stroke="#fff" stroke-width="3"/>
  <text x="52" y="37" text-anchor="middle" font-family="Lobster, cursive" font-size="17" fill="#fff">Best Offer</text>
</svg>
<div class="abs newsletter">Voyaro Deals Newsletter</div>
</body>
</html>
```